Vigilo Website

We are looking for a Wordpress designer to create an e-commerce website for us. We have all the products that will be uploaded to site on csv format, so our main focus is layout, style, home page slider image selections and related site page images selection by the designer.

When project is reaching completion we will provide product files.

Industry/Entity Type

E-Commerce

```html
<!DOCTYPE html>
<html lang="en">
<head>
<meta charset="utf-8">
<title>Vigilo – Accessories</title>
<link href="https://fonts.googleapis.com/css2?family=Open+Sans:wght@400;600;700&family=Montserrat:wght@500;600;700&display=swap" rel="stylesheet">
<style>
:root{
  --navy:#0d1b3d;
  --navy-2:#16264f;
  --blue:#1f6fe5;
  --blue-cta:#1c74f0;
  --text:#333a45;
  --muted:#8a909a;
  --line:#e6e8ec;
  --bg-soft:#f3f4f6;
  --red:#e0283a;
  --star:#f5b400;
}
*{box-sizing:border-box;margin:0;padding:0}
html,body{width:1200px;height:2404px;overflow:hidden}
body{font-family:"Open Sans",Arial,sans-serif;color:var(--text);background:#fff;font-size:13px;position:relative}
a{color:inherit;text-decoration:none}
ul{list-style:none}

/* header */
.topbar{height:36px;background:var(--navy);color:#c9d0de;font-size:11px;display:flex;justify-content:flex-end;align-items:center;gap:22px;padding-right:90px}
.mainbar{height:64px;background:#fff;display:flex;align-items:center;justify-content:space-between;padding:0 88px 0 0;box-shadow:0 1px 4px rgba(0,0,0,.06);position:relative}
.brand-slot{position:absolute;left:0;top:-36px;width:300px;height:100px;background:var(--navy);display:flex;align-items:center;padding-left:90px;gap:10px}
.brand-mark{width:26px;height:26px;background:var(--blue)}
.brand-name{font-family:"Montserrat",sans-serif;font-weight:700;font-size:26px;color:#fff;letter-spacing:1px}
.nav{margin-left:auto;display:flex;gap:28px;font-family:"Montserrat",sans-serif;font-size:12px;font-weight:600;color:#2d3340}
.nav .active{color:var(--blue)}
.nav-icons{display:flex;gap:14px;margin-left:30px}
.nav-icons svg{width:16px;height:16px}

/* banner */
.banner{height:132px;background:linear-gradient(100deg,#0c1a38 0%,#1d3566 55%,#122246 100%);display:flex;align-items:center;justify-content:space-between;padding:0 88px;color:#fff}
.banner h1{font-family:"Montserrat",sans-serif;font-size:22px;font-weight:700;letter-spacing:1px}
.crumbs{font-size:12px;display:flex;gap:8px;align-items:center;color:#dfe5f0}

/* layout */
.page{display:flex;gap:32px;padding:48px 80px 0 88px;height:1592px}
.sidebar{width:232px}
.content{width:768px}

.side-title{font-family:"Montserrat",sans-serif;font-size:14px;font-weight:700;color:#1b2233;margin-bottom:16px;letter-spacing:.5px}
.filter{margin-bottom:16px}
.filter h4{font-size:12px;font-weight:600;color:#1b2233;margin-bottom:8px}
.check{display:flex;align-items:center;gap:8px;font-size:11px;color:#555;margin-bottom:6px}
.check i{width:11px;height:11px;border:1px solid #bbb;display:inline-block}
.swatches{display:flex;gap:5px}
.swatches span{width:20px;height:14px;display:block}
.price-track{height:4px;background:#ddd;margin:12px 0 0;position:relative;width:200px}
.price-track::before{content:"";position:absolute;left:10px;right:20px;top:0;bottom:0;background:var(--blue)}
.price-track b{position:absolute;top:-5px;width:14px;height:14px;border-radius:50%;background:#fff;border:2px solid var(--blue)}

.mini{display:flex;gap:14px;align-items:center;margin-bottom:22px}
.mini .ph{width:72px;height:80px;background:linear-gradient(#f4f5f7,#cfd3d9)}
.mini h5{font-size:11px;font-weight:600;color:#2d3340;line-height:1.4}
.mini .stars{margin:4px 0}
.mini .price{font-size:13px;font-weight:700;color:#1b2233}
.mini .old{font-size:11px;color:var(--muted);text-decoration:line-through}
.btn-outline{display:inline-block;border:1px solid #2d3340;font-size:11px;font-weight:600;padding:7px 12px;color:#1b2233}
.btn-row{text-align:right;margin-bottom:36px}

.info-list li{font-size:11px;color:#555;margin-bottom:10px}

.stars{display:flex;gap:2px}
.stars svg{width:10px;height:10px;fill:var(--star)}
.stars svg.off{fill:#d5d7db}

/* content */
.content-head{display:flex;justify-content:space-between;align-items:baseline;margin-bottom:20px}
.content-head h2{font-family:"Montserrat",sans-serif;font-size:14px;font-weight:700;color:#1b2233}
.content-head span{font-size:11px;color:var(--muted)}
.toolbar{display:flex;align-items:center;border-bottom:1px solid var(--line);padding-bottom:10px;margin-bottom:18px;font-size:11px;color:#555}
.view{display:flex;gap:6px}
.view i{width:14px;height:14px;background:#cfd3d9;display:block}
.view i:first-child{background:#2d3340}
.sorts{margin-left:auto;display:flex;gap:18px;align-items:center}
.select{border:1px solid var(--line);padding:3px 24px 3px 8px}

.grid{display:grid;grid-template-columns:repeat(3,240px);column-gap:24px;row-gap:40px}
.card{text-align:center;position:relative}
.card .ph{height:300px;background:linear-gradient(#fafbfc,#e1e4e8);border:1px solid var(--line);position:relative}
.tag{position:absolute;top:10px;right:10px;background:#2d3340;color:#fff;font-size:9px;font-weight:700;padding:2px 6px}
.tag.sale{background:var(--red);top:auto;bottom:10px}
.card h3{font-size:12px;font-weight:600;color:#2d3340;margin:14px 0 6px}
.card .stars{justify-content:center;margin-bottom:6px}
.card .price{font-size:14px;font-weight:700;color:#1b2233}
.card .old{font-size:11px;color:var(--muted);text-decoration:line-through;margin-left:6px}

.pager{display:flex;align-items:center;margin-top:56px;font-size:11px;color:#555}
.pages{margin-left:auto;display:flex;gap:4px;align-items:center}
.pages span{min-width:22px;height:22px;border:1px solid var(--line);display:flex;align-items:center;justify-content:center;padding:0 6px}
.pages .cur{background:var(--blue);color:#fff;border-color:var(--blue)}
.pages .wide{margin-left:8px}

/* cta */
.cta{position:absolute;top:1824px;left:0;width:1200px;height:136px;background:var(--blue-cta);display:flex;align-items:center;justify-content:space-between;padding:0 120px 0 120px;color:#fff}
.cta p{font-family:"Montserrat",sans-serif;font-size:21px;font-weight:500}
.cta a{background:var(--navy);color:#fff;font-size:12px;font-weight:600;padding:14px 26px}

/* footer */
.footer{position:absolute;top:1960px;left:0;width:1200px;height:400px;background:var(--bg-soft);padding:72px 88px 0}
.footer-cols{display:flex}
.foot-brand{width:260px;display:flex;align-items:center;gap:10px;padding-top:60px}
.foot-brand .brand-mark{width:30px;height:30px}
.foot-brand .brand-name{color:var(--navy);font-size:30px}
.foot-col{width:260px}
.foot-col h4{font-family:"Montserrat",sans-serif;font-size:14px;font-weight:700;color:#1b2233;margin-bottom:18px}
.foot-col li{font-size:11px;color:#555;margin-bottom:14px;display:flex;gap:8px;align-items:center}
.foot-col li::before{content:"";width:4px;height:4px;background:var(--blue);display:block}
.feed-grid{display:grid;grid-template-columns:repeat(3,62px);gap:6px}
.feed-grid div{height:52px;background:linear-gradient(135deg,#4b5566,#a9b1bd)}
.contact li::before{display:none}
.contact li svg{width:12px;height:12px;fill:var(--blue);flex:none}
.bottom{position:absolute;top:2360px;left:0;width:1200px;height:44px;background:#fff;border-top:1px solid var(--line);display:flex;align-items:center;padding:0 88px;font-size:10px;color:var(--muted)}
.pay{display:flex;gap:6px;margin-left:300px}
.pay span{width:30px;height:18px;background:#dfe3ea;border-radius:2px;display:block}
.social{margin-left:auto;display:flex;gap:16px}
.social span{width:10px;height:10px;border-radius:50%;background:#7b8290;display:block}
</style>
</head>
<body>

<header>
  <div class="topbar"><span>My Account ▾</span><span>USD $ ▾</span><span>English ▾</span></div>
  <div class="mainbar">
    <div class="brand-slot"><span class="brand-mark"></span><span class="brand-name">Vigilo</span></div>
    <nav class="nav">
      <a class="active">Home</a><a>About Us</a><a>Services</a><a>Technology</a><a>Pages</a><a>Downloads</a><a>Contact Us</a>
    </nav>
    <div class="nav-icons">
      <svg viewBox="0 0 16 16"><circle cx="7" cy="7" r="5" fill="none" stroke="#2d3340" stroke-width="1.6"/><path d="M11 11l4 4" stroke="#2d3340" stroke-width="1.6"/></svg>
      <svg viewBox="0 0 16 16"><path d="M1 2h3l2 9h8l1-6H5" fill="none" stroke="#2d3340" stroke-width="1.5"/><circle cx="7" cy="14" r="1.3" fill="#2d3340"/><circle cx="13" cy="14" r="1.3" fill="#2d3340"/></svg>
    </div>
  </div>
</header>

<section class="banner" role="img" aria-label="Dark blue banner photo of security cameras">
  <h1>ACCESSORIES</h1>
  <div class="crumbs"><span>⌂</span><span>›</span><span>Accessories</span></div>
</section>

<main class="page">
  <aside class="sidebar">
    <h3 class="side-title">CATALOG</h3>
    <div class="filter"><h4>Condition</h4><div class="check"><i></i>New (20)</div></div>
    <div class="filter"><h4>Manufacturer</h4><div class="check"><i></i>Fashion Manufacturer (20)</div></div>
    <div class="filter"><h4>Size</h4><div class="check"><i></i>S (20)</div><div class="check"><i></i>M (20)</div><div class="check"><i></i>L (20)</div></div>
    <div class="filter"><h4>Color</h4>
      <div class="swatches"><span style="background:#d9d9d9"></span><span style="background:#2d3340"></span><span style="background:#8a6a4e"></span><span style="background:#f1e6cf"></span><span style="background:#5aa9e6"></span><span style="background:#e6c35a"></span><span style="background:#e68ab0"></span><span style="background:#f19a3e"></span></div>
    </div>
    <div class="filter"><h4>Styles</h4><div class="check"><i></i>Casual (8)</div><div class="check"><i></i>Dressy (6)</div><div class="check"><i></i>Girly (6)</div></div>
    <div class="filter" style="margin-bottom:64px"><h4>Price</h4><div class="check">Range: $16.00 – $73.00</div>
      <div class="price-track"><b style="left:4px"></b><b style="right:14px"></b></div></div>

    <h3 class="side-title">NEW PRODUCTS</h3>
    <div class="mini"><div class="ph" role="img" aria-label="Dome camera product photo"></div><div><h5>Adipcom Emit Vestibule</h5><div class="price">$103.00</div></div></div>
    <div class="mini"><div class="ph" role="img" aria-label="White security camera product photo"></div><div><h5>Datum Cortique Tristique</h5><div class="price">$84.00</div></div></div>
    <div class="mini"><div class="ph" role="img" aria-label="Outdoor camera product photo"></div><div><h5>Integer Tempor Lacus Eget</h5><div class="price">$99.00</div></div></div>
    <div class="btn-row"><a class="btn-outline">All New Products</a></div>

    <h3 class="side-title">INFORMATION</h3>
    <ul class="info-list" style="margin-bottom:34px">
      <li>Delivery</li><li>Legal Notice</li><li>Terms And Conditions Of Use</li><li>About Us</li><li>Secure Payment</li><li>Our Stores</li>
    </ul>

    <h3 class="side-title">SPECIALS</h3>
    <div class="mini"><div class="ph" role="img" aria-label="Security camera product photo"></div><div><h5>Nullus Neque Ut Enim</h5><div class="price">$153.00</div><div class="old">$180.00</div></div></div>
    <div class="btn-row"><a class="btn-outline">All Specials</a></div>
  </aside>

  <section class="content">
    <div class="content-head"><h2>Accessories</h2><span>There are 20 products.</span></div>
    <div class="toolbar">
      <div class="view"><i></i><i></i></div>
      <div class="sorts"><span>Show <span class="select">9</span> per page</span><span>Sort By <span class="select">–</span></span></div>
    </div>

    <div class="grid">
      <article class="card"><div class="ph" role="img" aria-label="Ceiling mount camera photo"><span class="tag">NEW</span></div><h3>Adventus Wellness Niva</h3><div class="stars"><svg viewBox="0 0 10 10"><path d="M5 0l1.5 3.2 3.5.4-2.6 2.3.8 3.5L5 7.6 1.8 9.4l.8-3.5L0 3.6l3.5-.4z"/></svg><svg viewBox="0 0 10 10"><path d="M5 0l1.5 3.2 3.5.4-2.6 2.3.8 3.5L5 7.6 1.8 9.4l.8-3.5L0 3.6l3.5-.4z"/></svg><svg viewBox="0 0 10 10"><path d="M5 0l1.5 3.2 3.5.4-2.6 2.3.8 3.5L5 7.6 1.8 9.4l.8-3.5L0 3.6l3.5-.4z"/></svg><svg viewBox="0 0 10 10"><path d="M5 0l1.5 3.2 3.5.4-2.6 2.3.8 3.5L5 7.6 1.8 9.4l.8-3.5L0 3.6l3.5-.4z"/></svg><svg class="off" viewBox="0 0 10 10"><path d="M5 0l1.5 3.2 3.5.4-2.6 2.3.8 3.5L5 7.6 1.8 9.4l.8-3.5L0 3.6l3.5-.4z"/></svg></div><div class="price">$105.00</div></article>
      <article class="card"><div class="ph" role="img" aria-label="Black pan tilt camera photo"><span class="tag">NEW</span></div><h3>Dom Nec Tristique Tempus</h3><div class="stars"><svg viewBox="0 0 10 10"><path d="M5 0l1.5 3.2 3.5.4-2.6 2.3.8 3.5L5 7.6 1.8 9.4l.8-3.5L0 3.6l3.5-.4z"/></svg><svg viewBox="0 0 10 10"><path d="M5 0l1.5 3.2 3.5.4-2.6 2.3.8 3.5L5 7.6 1.8 9.4l.8-3.5L0 3.6l3.5-.4z"/></svg><svg viewBox="0 0 10 10"><path d="M5 0l1.5 3.2 3.5.4-2.6 2.3.8 3.5L5 7.6 1.8 9.4l.8-3.5L0 3.6l3.5-.4z"/></svg><svg viewBox="0 0 10 10"><path d="M5 0l1.5 3.2 3.5.4-2.6 2.3.8 3.5L5 7.6 1.8 9.4l.8-3.5L0 3.6l3.5-.4z"/></svg><svg class="off" viewBox="0 0 10 10"><path d="M5 0l1.5 3.2 3.5.4-2.6 2.3.8 3.5L5 7.6 1.8 9.4l.8-3.5L0 3.6l3.5-.4z"/></svg></div><div class="price">$152.00</div></article>
      <article class="card"><div class="ph" role="img" aria-label="White indoor camera photo"><span class="tag">NEW</span></div><h3>Habitasse Platea Dictumst</h3><div class="stars"><svg viewBox="0 0 10 10"><path d="M5 0l1.5 3.2 3.5.4-2.6 2.3.8 3.5L5 7.6 1.8 9.4l.8-3.5L0 3.6l3.5-.4z"/></svg><svg viewBox="0 0 10 10"><path d="M5 0l1.5 3.2 3.5.4-2.6 2.3.8 3.5L5 7.6 1.8 9.4l.8-3.5L0 3.6l3.5-.4z"/></svg><svg viewBox="0 0 10 10"><path d="M5 0l1.5 3.2 3.5.4-2.6 2.3.8 3.5L5 7.6 1.8 9.4l.8-3.5L0 3.6l3.5-.4z"/></svg><svg viewBox="0 0 10 10"><path d="M5 0l1.5 3.2 3.5.4-2.6 2.3.8 3.5L5 7.6 1.8 9.4l.8-3.5L0 3.6l3.5-.4z"/></svg><svg class="off" viewBox="0 0 10 10"><path d="M5 0l1.5 3.2 3.5.4-2.6 2.3.8 3.5L5 7.6 1.8 9.4l.8-3.5L0 3.6l3.5-.4z"/></svg></div><div class="price">$97.00</div></article>

      <article class="card"><div class="ph" role="img" aria-label="White cylinder camera photo"><span class="tag">NEW</span></div><h3>Praesent Fringilla Augue</h3><div class="stars"><svg viewBox="0 0 10 10"><path d="M5 0l1.5 3.2 3.5.4-2.6 2.3.8 3.5L5 7.6 1.8 9.4l.8-3.5L0 3.6l3.5-.4z"/></svg><svg viewBox="0 0 10 10"><path d="M5 0l1.5 3.2 3.5.4-2.6 2.3.8 3.5L5 7.6 1.8 9.4l.8-3.5L0 3.6l3.5-.4z"/></svg><svg viewBox="0 0 10 10"><path d="M5 0l1.5 3.2 3.5.4-2.6 2.3.8 3.5L5 7.6 1.8 9.4l.8-3.5L0 3.6l3.5-.4z"/></svg><svg viewBox="0 0 10 10"><path d="M5 0l1.5 3.2 3.5.4-2.6 2.3.8 3.5L5 7.6 1.8 9.4l.8-3.5L0 3.6l3.5-.4z"/></svg><svg class="off" viewBox="0 0 10 10"><path d="M5 0l1.5 3.2 3.5.4-2.6 2.3.8 3.5L5 7.6 1.8 9.4l.8-3.5L0 3.6l3.5-.4z"/></svg></div><div class="price">$99.00</div></article>
      <article class="card"><div class="ph" role="img" aria-label="Black wireless camera photo"><span class="tag">NEW</span><span class="tag sale">SALE</span></div><h3>Arcu Vitae Imperdiet Facilisis</h3><div class="stars"><svg viewBox="0 0 10 10"><path d="M5 0l1.5 3.2 3.5.4-2.6 2.3.8 3.5L5 7.6 1.8 9.4l.8-3.5L0 3.6l3.5-.4z"/></svg><svg viewBox="0 0 10 10"><path d="M5 0l1.5 3.2 3.5.4-2.6 2.3.8 3.5L5 7.6 1.8 9.4l.8-3.5L0 3.6l3.5-.4z"/></svg><svg viewBox="0 0 10 10"><path d="M5 0l1.5 3.2 3.5.4-2.6 2.3.8 3.5L5 7.6 1.8 9.4l.8-3.5L0 3.6l3.5-.4z"/></svg><svg viewBox="0 0 10 10"><path d="M5 0l1.5 3.2 3.5.4-2.6 2.3.8 3.5L5 7.6 1.8 9.4l.8-3.5L0 3.6l3.5-.4z"/></svg><svg class="off" viewBox="0 0 10 10"><path d="M5 0l1.5 3.2 3.5.4-2.6 2.3.8 3.5L5 7.6 1.8 9.4l.8-3.5L0 3.6l3.5-.4z"/></svg></div><div class="price">$98.00<span class="old">$115.00</span></div></article>
      <article class="card"><div class="ph" role="img" aria-label="Black pan tilt camera photo"><span class="tag">NEW</span></div><h3>Curabitur Dolor Nunc</h3><div class="stars"><svg viewBox="0 0 10 10"><path d="M5 0l1.5 3.2 3.5.4-2.6 2.3.8 3.5L5 7.6 1.8 9.4l.8-3.5L0 3.6l3.5-.4z"/></svg><svg viewBox="0 0 10 10"><path d="M5 0l1.5 3.2 3.5.4-2.6 2.3.8 3.5L5 7.6 1.8 9.4l.8-3.5L0 3.6l3.5-.4z"/></svg><svg viewBox="0 0 10 10"><path d="M5 0l1.5 3.2 3.5.4-2.6 2.3.8 3.5L5 7.6 1.8 9.4l.8-3.5L0 3.6l3.5-.4z"/></svg><svg viewBox="0 0 10 10"><path d="M5 0l1.5 3.2 3.5.4-2.6 2.3.8 3.5L5 7.6 1.8 9.4l.8-3.5L0 3.6l3.5-.4z"/></svg><svg class="off" viewBox="0 0 10 10"><path d="M5 0l1.5 3.2 3.5.4-2.6 2.3.8 3.5L5 7.6 1.8 9.4l.8-3.5L0 3.6l3.5-.4z"/></svg></div><div class="price">$101.00</div></article>

      <article class="card"><div class="ph" role="img" aria-label="Tall slim camera photo"><span class="tag">NEW</span><span class="tag sale">SALE</span></div><h3>Dum Gravis Volutpat</h3><div class="stars"><svg viewBox="0 0 10 10"><path d="M5 0l1.5 3.2 3.5.4-2.6 2.3.8 3.5L5 7.6 1.8 9.4l.8-3.5L0 3.6l3.5-.4z"/></svg><svg viewBox="0 0 10 10"><path d="M5 0l1.5 3.2 3.5.4-2.6 2.3.8 3.5L5 7.6 1.8 9.4l.8-3.5L0 3.6l3.5-.4z"/></svg><svg viewBox="0 0 10 10"><path d="M5 0l1.5 3.2 3.5.4-2.6 2.3.8 3.5L5 7.6 1.8 9.4l.8-3.5L0 3.6l3.5-.4z"/></svg><svg viewBox="0 0 10 10"><path d="M5 0l1.5 3.2 3.5.4-2.6 2.3.8 3.5L5 7.6 1.8 9.4l.8-3.5L0 3.6l3.5-.4z"/></svg><svg class="off" viewBox="0 0 10 10"><path d="M5 0l1.5 3.2 3.5.4-2.6 2.3.8 3.5L5 7.6 1.8 9.4l.8-3.5L0 3.6l3.5-.4z"/></svg></div><div class="price">$123.20<span class="old">$154.00</span></div></article>
      <article class="card"><div class="ph" role="img" aria-label="Black smart hub device photo"><span class="tag">NEW</span></div><h3>Suspendisse Massa Nulla</h3><div class="stars"><svg viewBox="0 0 10 10"><path d="M5 0l1.5 3.2 3.5.4-2.6 2.3.8 3.5L5 7.6 1.8 9.4l.8-3.5L0 3.6l3.5-.4z"/></svg><svg viewBox="0 0 10 10"><path d="M5 0l1.5 3.2 3.5.4-2.6 2.3.8 3.5L5 7.6 1.8 9.4l.8-3.5L0 3.6l3.5-.4z"/></svg><svg viewBox="0 0 10 10"><path d="M5 0l1.5 3.2 3.5.4-2.6 2.3.8 3.5L5 7.6 1.8 9.4l.8-3.5L0 3.6l3.5-.4z"/></svg><svg viewBox="0 0 10 10"><path d="M5 0l1.5 3.2 3.5.4-2.6 2.3.8 3.5L5 7.6 1.8 9.4l.8-3.5L0 3.6l3.5-.4z"/></svg><svg class="off" viewBox="0 0 10 10"><path d="M5 0l1.5 3.2 3.5.4-2.6 2.3.8 3.5L5 7.6 1.8 9.4l.8-3.5L0 3.6l3.5-.4z"/></svg></div><div class="price">$112.00</div></article>
      <article class="card"><div class="ph" role="img" aria-label="White indoor camera photo"><span class="tag">NEW</span></div><h3>Lorem Neque Commodo Est</h3><div class="stars"><svg viewBox="0 0 10 10"><path d="M5 0l1.5 3.2 3.5.4-2.6 2.3.8 3.5L5 7.6 1.8 9.4l.8-3.5L0 3.6l3.5-.4z"/></svg><svg viewBox="0 0 10 10"><path d="M5 0l1.5 3.2 3.5.4-2.6 2.3.8 3.5L5 7.6 1.8 9.4l.8-3.5L0 3.6l3.5-.4z"/></svg><svg viewBox="0 0 10 10"><path d="M5 0l1.5 3.2 3.5.4-2.6 2.3.8 3.5L5 7.6 1.8 9.4l.8-3.5L0 3.6l3.5-.4z"/></svg><svg viewBox="0 0 10 10"><path d="M5 0l1.5 3.2 3.5.4-2.6 2.3.8 3.5L5 7.6 1.8 9.4l.8-3.5L0 3.6l3.5-.4z"/></svg><svg class="off" viewBox="0 0 10 10"><path d="M5 0l1.5 3.2 3.5.4-2.6 2.3.8 3.5L5 7.6 1.8 9.4l.8-3.5L0 3.6l3.5-.4z"/></svg></div><div class="price">$96.00</div></article>
    </div>

    <div class="pager">
      <span>Showing 1 – 9 of 20 items</span>
      <div class="pages"><span>‹</span><span class="cur">1</span><span>2</span><span>3</span><span>›</span><span class="wide">Show All</span><span class="wide">Compare (0)</span></div>
    </div>
  </section>
</main>

<section class="cta">
  <p>2000+ people have put their trust in Vigilo. How about you?</p>
  <a>Get Started Now</a>
</section>

<footer class="footer">
  <div class="footer-cols">
    <div class="foot-brand"><span class="brand-mark"></span><span class="brand-name">Vigilo</span></div>
    <div class="foot-col">
      <h4>Important Links</h4>
      <ul><li>Support</li><li>Privacy &amp; Policy</li><li>Terms &amp; Conditions</li><li>Catalogue</li><li>Our Network</li></ul>
    </div>
    <div class="foot-col">
      <h4>Feedback</h4>
      <div class="feed-grid" role="img" aria-label="Grid of customer photos">
        <div></div><div></div><div></div><div></div><div></div><div></div>
      </div>
    </div>
    <div class="foot-col contact">
      <h4>Contact with us</h4>
      <ul>
        <li><svg viewBox="0 0 12 12"><path d="M6 0a4 4 0 0 1 4 4c0 3-4 8-4 8S2 7 2 4a4 4 0 0 1 4-4zm0 2.5a1.5 1.5 0 1 0 0 3 1.5 1.5 0 0 0 0-3z"/></svg>48 Harbor Lane, Westfield</li>
        <li><svg viewBox="0 0 12 12"><path d="M2.5 0l2 3-1.2 1.3a7 7 0 0 0 4.4 4.4L9 7.5l3 2-1.5 2.5C5 12 0 7 0 1.5z"/></svg>+1 555 0142 880</li>
        <li><svg viewBox="0 0 12 12"><path d="M0 2h12v8H0zm1 1l5 3.5L11 3z"/></svg>hello@vigilo-store.com</li>
      </ul>
    </div>
  </div>
</footer>

<div class="bottom">
  <span>Copyright © 2017. All rights reserved.</span>
  <div class="pay"><span></span><span></span><span></span><span></span><span></span></div>
  <div class="social"><span></span><span></span><span></span><span></span><span></span></div>
</div>

</body>
</html>
```